Website Redesign Project Puzzle Vault Leesburg

We are an escape room company located in Ashburn, Virginia. We currently have a website https://www.puzzlevaultleesburg.example based upon html/bootstrap/javascript/php/mysql and I'd like to keep it that way. I'm looking for someone upgrade the front page so it is more informative, cleaner, quicker to load, and optimizes the space for full sale opportunities.

Target Market(s)

Corporate Clients, Families, Friends. All ages

Industry/Entity Type

Entertainment Industry

Coding

Font styles to use
Other font styles liked:
• Similar to Facebook or Amazon

Requirements
Must have
• Must be mobile friendly. bootstrap. Lots of graphics (will provide) nice and easy to read fonts. Easy to read layout. Must look clean, fresh, exciting, and want to grab attention.
• Please visit my facebook page and website for more details. facebook.com/puzzlevaultleesburg
Nice to have
• Same color as existing but open to options if they look nice.
Should not have
• Should not be wordpress or hard to modify.

```html
<!DOCTYPE html>
<html lang="en">
<head>
<meta charset="utf-8">
<title>Puzzle Vault Leesburg</title>
<link rel="stylesheet" href="https://fonts.googleapis.com/css2?family=Open+Sans:wght@400;600;700;800&display=swap">
<style>
:root{
  --blue:#13a3e3;
  --blue-dark:#0e8fca;
  --ink:#1d1d1f;
  --text:#4a4a4a;
  --muted:#8a8f99;
  --grey-bg:#ebedf1;
  --field:#f1f2f4;
  --line:#dcdfe4;
  --header:#050505;
  --white:#fff;
}
*{box-sizing:border-box;margin:0;padding:0}
html,body{width:1200px;height:3701px;overflow:hidden}
body{font-family:"Open Sans",Arial,sans-serif;color:var(--text);background:var(--white);position:relative}
.abs{position:absolute}
.btn{display:inline-flex;align-items:center;justify-content:center;background:var(--blue);color:var(--white);font-weight:700;text-transform:uppercase;border-radius:3px;letter-spacing:.3px}
.section-title{position:absolute;left:0;width:1200px;text-align:center;color:var(--blue);font-weight:700;font-size:24px;letter-spacing:.3px}

/* header */
.site-header{position:absolute;left:0;top:0;width:1200px;height:83px;background:var(--header)}
.brand{position:absolute;left:149px;top:18px;display:flex;align-items:center;gap:8px;color:var(--blue);font-weight:800;font-size:17px;line-height:1.05;width:130px}
.brand-mark{width:14px;height:14px;border:2px solid var(--blue);flex:none}
.main-nav a{position:absolute;top:33px;color:var(--white);font-size:13px;font-weight:600;text-decoration:none;letter-spacing:.2px}
.main-nav a.active{color:var(--blue)}
.header-book{position:absolute;left:940px;top:24px;width:109px;height:35px;font-size:13px}

/* hero */
.hero{position:absolute;left:0;top:83px;width:1200px;height:423px;background:linear-gradient(180deg,#4a4a4c 0%,#3c3c3e 58%,#6c5a46 75%,#2f2620 100%)}
.hero-door{position:absolute;left:517px;top:48px;width:161px;height:281px;border:4px solid var(--blue);background:linear-gradient(180deg,#1b1b1b,#0c0c0c)}
.hero-book{position:absolute;left:532px;top:351px;width:129px;height:43px;font-size:14px}

/* rooms */
.rooms{position:absolute;left:0;top:506px;width:1200px;height:1060px;background:var(--grey-bg)}
.room-card{position:absolute;width:286px;height:446px;background:var(--white);border:1px solid var(--line);text-align:center}
.room-photo{width:100%;height:224px}
.room-card h3{font-size:18px;font-weight:600;color:var(--ink);margin-top:18px;letter-spacing:.3px}
.room-card .desc{font-size:10.5px;font-weight:600;line-height:18px;padding:0 20px;margin-top:10px;height:72px}
.room-card .price{font-size:13.5px;color:var(--text);margin-top:4px;word-spacing:2px}
.room-card .price span{margin-left:18px}
.room-card .btn{position:absolute;left:92px;top:391px;width:102px;height:33px;font-size:11px}

/* events */
.events{position:absolute;left:0;top:1566px;width:1200px;height:762px;background:var(--white)}
.events-intro{position:absolute;left:200px;top:84px;width:800px;text-align:center;font-size:13.5px;line-height:23px}
.event{position:absolute;top:181px;width:164px;text-align:center}
.event-ring{width:164px;height:164px;border:3px solid var(--blue);border-radius:50%;display:flex;align-items:center;justify-content:center}
.event-art{width:84px;height:84px;border-radius:50%}
.event h4{margin-top:22px;font-size:13px;font-weight:700;color:var(--ink);letter-spacing:.4px;white-space:nowrap;margin-left:-30px;margin-right:-30px}
.field{position:absolute;background:var(--field);border:1px solid var(--line);border-radius:2px;font-size:12px;color:var(--muted);padding:10px 14px}
.field.white{background:var(--white)}

/* how it works */
.how{position:absolute;left:0;top:2328px;width:1200px;height:560px;background:var(--grey-bg)}
.faq{position:absolute;width:289px;background:var(--white);text-align:center;padding:10px 12px}
.faq h4{font-size:14.5px;font-weight:600;color:var(--ink);line-height:20px}
.faq p{font-size:10.5px;line-height:18px;margin-top:6px}
.faq a{display:block;color:var(--blue);font-weight:700;font-size:10.5px;text-decoration:none}

/* location */
.location{position:absolute;left:0;top:2888px;width:1200px;height:410px;background:var(--white)}
.map{position:absolute;left:149px;top:84px;width:443px;height:266px;background:linear-gradient(135deg,#e9ebee 0%,#e3e6ea 60%,#cfe6c7 100%);border:1px solid var(--line)}
.info{position:absolute;left:630px;width:396px;text-align:center;color:var(--ink)}
.info h4{font-size:14px;font-weight:700;letter-spacing:.3px}
.info p{font-size:14px;line-height:26px;margin-top:4px}
.info-rule{position:absolute;left:688px;top:92px;width:280px;height:1px;background:var(--line)}

/* contact */
.contact{position:absolute;left:0;top:3298px;width:1200px;height:403px;background:var(--grey-bg)}
.contact-line{position:absolute;left:0;top:80px;width:1200px;text-align:center;font-size:13.5px}
.contact-line b{color:var(--ink);font-weight:600}
.copyright{position:absolute;left:149px;top:377px;font-size:9px;color:var(--text)}
.social{position:absolute;top:371px;width:20px;height:20px;border-radius:50%;background:var(--blue)}
</style>
</head>
<body>

<header class="site-header">
  <div class="brand"><span class="brand-mark"></span><span>Puzzle Vault Leesburg</span></div>
  <nav class="main-nav">
    <a class="active" style="left:295px">ESCAPE ROOMS</a>
    <a style="left:434px">SPECIAL EVENTS</a>
    <a style="left:575px">HOW IT WORKS</a>
    <a style="left:714px">LOCATION</a>
    <a style="left:819px">CONTACT US</a>
  </nav>
  <span class="btn header-book">Book Now</span>
</header>

<section class="hero" role="img" aria-label="Hallway of wooden doors with a glowing maze door in the centre">
  <div class="hero-door" role="img" aria-label="Maze-patterned door with a key"></div>
  <span class="btn hero-book">Book Now</span>
</section>

<section class="rooms">
  <h2 class="section-title" style="top:30px">CHOOSE YOUR OWN ESCAPE ROOM</h2>

  <article class="room-card" style="left:149px;top:83px">
    <div class="room-photo" role="img" aria-label="Group photo inside the elevator room" style="background:linear-gradient(160deg,#3a1a4a,#b0304a 55%,#2a1830)"></div>
    <h3>ELEVATOR</h3>
    <p class="desc">The main elevators are down so you'll need to take the freight elevator to the top floor if you want to get your award. The last celebrity that attempted to do so wasn't so lucky.</p>
    <p class="price">$28.00/person.<span>Min: 4 Max: 6</span></p>
    <span class="btn">Book Now</span>
  </article>

  <article class="room-card" style="left:457px;top:83px">
    <div class="room-photo" role="img" aria-label="Presidential seal with a golden microphone" style="background:linear-gradient(160deg,#c9ccd6,#1f2a55 50%,#b89a4a)"></div>
    <h3>THE SPEECH</h3>
    <p class="desc">The President's speech has been hijacked and replaced with lyrics from an 80s hit song. Your task is to go in and find the correct speech before he takes the podium.</p>
    <p class="price">$28.00/person.<span>Min: 4 Max: 8</span></p>
    <span class="btn">Book Now</span>
  </article>

  <article class="room-card" style="left:763px;top:83px">
    <div class="room-photo" role="img" aria-label="Purple bank vault door" style="background:linear-gradient(160deg,#6a5a92,#3c2f5c 60%,#8a7bb0)"></div>
    <h3>BANK HEIST</h3>
    <p class="desc">With your family held hostage, the mob gave you one choice - rob the bank in exchange for their freedom or its goodbyes forever.</p>
    <p class="price">$28.00/person.<span>Min:2 Max: 8</span></p>
    <span class="btn">Book Now</span>
  </article>

  <article class="room-card" style="left:149px;top:553px">
    <div class="room-photo" role="img" aria-label="Group in orange jumpsuits in the jail room" style="background:linear-gradient(160deg,#2e3034,#d2541e 55%,#3a3a3a)"></div>
    <h3>JAIL BREAK</h3>
    <p class="desc">One Guard, One Goal: get out.</p>
    <p class="price">$28.00/person.<span>Min: 2 Max: 6</span></p>
    <span class="btn">Book Now</span>
  </article>

  <article class="room-card" style="left:457px;top:553px">
    <div class="room-photo" role="img" aria-label="Candy shop room with striped walls and candy tubes" style="background:linear-gradient(90deg,#c7cde8,#eef0f6 30%,#c7cde8 60%,#eef0f6)"></div>
    <h3>CANDY SHOP</h3>
    <p class="desc">With all of the candy right before your eyes, find the golden ticket and win the prize!</p>
    <p class="price">$28.00/person.<span>Min: 2 Max: 8</span></p>
    <span class="btn">Book Now</span>
  </article>

  <article class="room-card" style="left:763px;top:553px">
    <div class="room-photo" role="img" aria-label="Large group of guests posing together" style="background:linear-gradient(160deg,#1f2f3e,#8a7a6c 55%,#c9b59c)"></div>
    <h3>MORE TO COME</h3>
    <p class="desc">Visit our website regularly because we'll update our rooms in the future. Now, just try one of our adventureful rooms.</p>
    <p class="price">&nbsp;</p>
    <span class="btn">Book Now</span>
  </article>
</section>

<section class="events">
  <h2 class="section-title" style="top:32px">SPECIAL EVENTS</h2>
  <p class="events-intro">Puzzle Vault Leesburg is the perfect place to gather groups of colleagues, friends, or family and experience the latest entertainment in town. Simply complete the form below and our specialist will contact you for further details. Group pricing is available on group parties.</p>

  <div class="event" style="left:149px">
    <div class="event-ring"><div class="event-art" role="img" aria-label="Red heart illustration" style="background:#e0283c"></div></div>
    <h4>CORPORATE MEETINGS</h4>
  </div>
  <div class="event" style="left:395px">
    <div class="event-ring"><div class="event-art" role="img" aria-label="Pink birthday cake illustration" style="background:linear-gradient(180deg,#f6a3c4,#e8558f)"></div></div>
    <h4>BIRTHDAY PARTIES</h4>
  </div>
  <div class="event" style="left:639px">
    <div class="event-art-wrap"></div>
    <div class="event-ring" style="margin-top:-0px"><div class="event-art" role="img" aria-label="Colourful balloons illustration" style="background:linear-gradient(135deg,#f7d516,#e32c8c 50%,#4ac3d8)"></div></div>
    <h4>ANNIVERSARIES</h4>
  </div>
  <div class="event" style="left:884px">
    <div class="event-ring"><div class="event-art" role="img" aria-label="Party hat illustration" style="background:linear-gradient(160deg,#f2c23a,#e8472e)"></div></div>
    <h4>HOLIDAYS</h4>
  </div>

  <div class="field" style="left:149px;top:418px;width:442px;height:37px">Your Name *</div>
  <div class="field" style="left:149px;top:463px;width:442px;height:37px">Company Name</div>
  <div class="field" style="left:149px;top:508px;width:442px;height:37px">Your Email *</div>
  <div class="field" style="left:149px;top:553px;width:442px;height:37px">Size of Party</div>
  <div class="field" style="left:149px;top:598px;width:442px;height:37px">Your Phone *</div>
  <div class="field" style="left:608px;top:418px;width:441px;height:217px">Your Message *</div>
  <span class="btn abs" style="left:539px;top:666px;width:122px;height:34px;font-size:10.5px">Send Message</span>
</section>

<section class="how">
  <h2 class="section-title" style="top:30px">HOW IT WORKS</h2>

  <div class="faq" style="left:149px;top:85px;height:133px"><h4>How do I make a reservation?</h4><p>Click on the Book now button or click here.</p><a>Book Now</a></div>
  <div class="faq" style="left:454px;top:85px;height:133px"><h4>How long does an escape last?</h4><p>Each escape lasts 60 minutes.</p></div>
  <div class="faq" style="left:759px;top:85px;height:133px;width:290px"><h4>Is there an age limit?</h4><p>Participants 12 and older can be by themselves as long as an adult signs the waivers and is available for emergencies. Participants under 12 must be accompanied by an adult in the room or at the facility.</p></div>

  <div class="faq" style="left:149px;top:234px;height:134px"><h4>I'm pregnant, can I participate?</h4><p>Less than 8 months yes.</p></div>
  <div class="faq" style="left:454px;top:234px;height:134px"><h4>How can I redeem a voucher or promo code?</h4><p>Click on the Book Now button and enter the code in the promo code text box.</p></div>
  <div class="faq" style="left:759px;top:234px;height:134px;width:290px"><h4>Where do I park?</h4><p>Plenty of parking in front of the building</p></div>

  <div class="faq" style="left:149px;top:385px;height:118px"><h4>Do I have to sign a liability waiver?</h4><p>Yes. You can find the liability waiver here.</p><a>Click here for waiver</a></div>
  <div class="faq" style="left:454px;top:385px;height:118px"><h4>Which room is the most challenging?</h4><p>They are all challenging!</p></div>
  <div class="faq" style="left:759px;top:385px;height:118px;width:290px"><h4>What is the cancellation policy?</h4><p>24 hours notice from the scheduled reservation date. If you don't cancel within 24 hours you will lose your reservation and payment.</p></div>
</section>

<section class="location">
  <h2 class="section-title" style="top:30px">LOCATION</h2>
  <div class="map" role="img" aria-label="Street map showing the venue location"></div>
  <div class="info-rule"></div>
  <div class="info" style="top:108px"><h4>ADDRESS</h4><p>1150 Harrow Mill Road, Suite 12 Leesburg, VA 20175</p></div>
  <div class="info" style="top:174px"><h4>PHONE NUMBER</h4><p>(555) 014 2290</p></div>
  <div class="info" style="top:239px"><h4>HOURS</h4><p>Wednesday - Friday : 4pm - 10pm<br>Saturday : 11am - 11pm<br>Sunday : 11am - 9:30pm.</p></div>
</section>

<section class="contact">
  <h2 class="section-title" style="top:30px">CONTACT US</h2>
  <p class="contact-line">Call <b>555 014 2290</b> &nbsp;or &nbsp;Send Us a Message.</p>
  <div class="field white" style="left:149px;top:119px;width:442px;height:36px">Your Name</div>
  <div class="field white" style="left:149px;top:164px;width:442px;height:36px">Your Email</div>
  <div class="field white" style="left:149px;top:208px;width:442px;height:36px">Your Phone</div>
  <div class="field white" style="left:608px;top:119px;width:441px;height:125px">We'd love to hear from you. We'll get back to you immediately.</div>
  <span class="btn abs" style="left:557px;top:267px;width:86px;height:33px;font-size:10.5px">Submit</span>
  <p class="copyright">Copyright @ Puzzle Vault Leesburg</p>
  <span class="social" style="left:957px"></span>
  <span class="social" style="left:981px"></span>
  <span class="social" style="left:1005px"></span>
  <span class="social" style="left:1029px"></span>
</section>

</body>
</html>
```